Business card - Brio Margin - size 85 mm * 55 mm

We need new business cards. Design must fit with our vision of the firm. You find in the attached file our logo and a short description of our firm (mission, vision, value, business and so on).

Target Market(s)

Consulting firm in performance improvement

Industry/Entity Type

Management Consulting

Contact Information for Business Card

SIZE
85 mm * 55 mm
INFORMATIONS
name surname
role position
telephone number
email address

Requirements
Must have
• the brand must APPEAR for the rest Would we like to have something sleek, inspired to a "just right" approach
Should not have
• Please avoid the black color as background

```html
<!DOCTYPE html>
<html lang="en">
<head>
<meta charset="utf-8">
<title>Brio Margin – Business Card</title>
<link href="https://fonts.googleapis.com/css2?family=Lato:wght@400;700&display=swap" rel="stylesheet">
<style>
  :root {
    --page: #e9e7e4;
    --card-top: #f4f6f8;
    --card-bottom: #e2e8ee;
    --brand: #d8512b;
    --brand-deep: #c7401d;
    --band-light: #e8643c;
    --ink-light: #e9e4df;
    --ink-dark: #3c2a24;
  }
  * { margin: 0; padding: 0; box-sizing: border-box; }
  html, body {
    width: 1200px; height: 970px; overflow: hidden;
    background: var(--page);
    font-family: "Lato", sans-serif;
  }
  .card {
    position: absolute; left: 100px; top: 161px;
    width: 1000px; height: 647px;
    background: linear-gradient(160deg, var(--card-top), var(--card-bottom));
    overflow: hidden;
    box-shadow: 0 10px 30px rgba(0,0,0,0.12);
  }
  .brand-mark {
    position: absolute; left: 157px; top: 63px;
    width: 212px; height: 212px;
    border: 6px solid var(--brand); border-radius: 50%;
    display: flex; flex-direction: column; align-items: center; justify-content: center;
    color: var(--brand); font-weight: 700; font-size: 40px; line-height: 1.05;
    text-transform: uppercase; letter-spacing: 2px; text-align: center;
  }
  .brand-name {
    position: absolute; left: 61px; top: 288px;
    font-size: 38px; font-weight: 400; letter-spacing: 15px;
    color: var(--brand); text-transform: uppercase; white-space: nowrap;
  }
  .contact-band {
    position: absolute; left: 0; top: 389px;
    width: 600px; height: 258px;
    background: linear-gradient(90deg, var(--brand-deep), var(--band-light) 45%, var(--brand));
  }
  .person-name {
    position: absolute; left: 61px; top: 412px;
    font-size: 37px; font-weight: 400; color: var(--ink-light);
    letter-spacing: 0.5px;
  }
  .person-role {
    position: absolute; left: 61px; top: 455px;
    font-size: 27px; color: var(--ink-dark);
  }
  .contact-line {
    position: absolute; left: 61px;
    display: flex; align-items: center; gap: 12px;
    font-size: 29px; color: var(--ink-dark);
  }
  .contact-line.phone { top: 522px; }
  .contact-line.email { top: 564px; }
  .contact-icon { width: 30px; height: 30px; flex: none; }
  .deco-mark {
    position: absolute; left: 597px; top: 208px;
    width: 420px; height: 420px;
    border: 9px solid var(--brand); border-radius: 50%;
    background: var(--card-bottom);
    display: flex; flex-direction: column; justify-content: center;
    padding-left: 48px;
    color: var(--brand); font-weight: 700; font-size: 92px; line-height: 1;
    text-transform: uppercase; letter-spacing: 3px; white-space: nowrap;
    opacity: 0.9;
  }
</style>
</head>
<body>
  <div class="card">
    <div class="brand-mark"><span>Brio</span><span>Margin</span></div>
    <div class="brand-name">Brio Margin</div>

    <div class="contact-band"></div>
    <div class="deco-mark"><span>Brio</span><span>Margin</span></div>

    <div class="person-name">LENA HART</div>
    <div class="person-role">Chief Executive Officer</div>

    <div class="contact-line phone">
      <svg class="contact-icon" viewBox="0 0 30 30" aria-hidden="true">
        <circle cx="15" cy="15" r="15" fill="#e9e4df"/>
        <path d="M11 8l3 4-2 2c1 2 3 4 5 5l2-2 4 3-2 3c-6 0-12-6-12-12z" fill="#c7401d"/>
      </svg>
      <span>555 014 2290</span>
    </div>
    <div class="contact-line email">
      <svg class="contact-icon" viewBox="0 0 30 30" aria-hidden="true">
        <circle cx="15" cy="15" r="15" fill="#e9e4df"/>
        <rect x="7" y="10" width="16" height="11" fill="none" stroke="#c7401d" stroke-width="2"/>
        <path d="M7 10l8 6 8-6" fill="none" stroke="#c7401d" stroke-width="2"/>
      </svg>
      <span>lena@briomargin.com</span>
    </div>
  </div>
</body>
</html>
```